Opan Skies Field Learning Travel Brochure

I'm looking for a brochure design for a new travel product - Open Skies Field Learning, catering for students above 12 years old. Target audience are schools that do destination projects. Brochure to be read by head teacher, parents and students.

Brochure should be A4 in size, 4-6 pages. Format of brochure is hard cover (a folder) with inlet for flyers. Flyers for destinations will be updated from time to time.

Finished job needs to be converted to electronic format for website and email proposal usage.

Attached is text to be used on brochure. Order of section can be adjusted.

For "Elements of the trip", please understand the contents and explain/display it in a graphic form.

For flyer, please come out with a template that I can use for other destinations. The main elements - what's included, number of days, location for pictures, itinerary, educational focus, should be alterable. Attached are text for two sample destinations.
Also attached (tour itinerary example) a version of flyer that I like.

I'm attaching some pictures here. If you find more suitable pictures, please feel free to use them.
Updates

Reason: I'm extending the deadline of this project by 4 days, as I need to add details & photo of another travel specialist in personnel session (total of 3 members). Also, in view of the amount of work a designer has to do for this project, I'm giving you more time for submission. Please do not hesitate to be in touch should you need more than 4 days extension. Thank you.

Target Market(s)

Schools - especially the head teacher and parents, to send students above 12 years old to travel

Industry/Entity Type

Electronic

Requirements
Must have
• This is a travel brochure with education elements in it. Parents feel better when their children are travelling for a purpose and lead by responsible teachers/adults whom they can trust. So, the design has to emphasis that education elements and safety are our utmost priority.
Nice to have
• We specialise in environmental study. So, it is nice to have the environmental touch in the design.
Should not have
• Our target market segment is the Middle East, which can be quite sensitive to religion. I prefer not to have any religious related illustration on the design.

```html
<!DOCTYPE html>
<html lang="en">
<head>
<meta charset="utf-8">
<title>Cairo &amp; Luxor Tour Flyer</title>
<link rel="stylesheet" href="https://fonts.googleapis.com/css2?family=Arimo:ital,wght@0,400;0,700;1,700&display=swap">
<style>
:root{
  --navy:#1b3766;
  --blue:#1f4e8c;
  --ink:#3a3f47;
  --muted:#6b7079;
  --panel-a:#eef1f5;
  --panel-b:#dfe4ec;
  --box:#e6e8ec;
  --white:#ffffff;
  --sand-a:#d9b47d;
  --sand-b:#a77a44;
  --sky-a:#9fc3e3;
  --sky-b:#e8d4ac;
  --stone-a:#cdb48c;
  --stone-b:#8c6a43;
}
*{margin:0;padding:0;box-sizing:border-box}
html,body{width:1200px;height:488px;overflow:hidden;background:var(--white)}
body{font-family:"Arimo",Arial,sans-serif;color:var(--ink);position:relative}
.page{position:absolute;top:0;height:488px;width:396px;background:var(--white);overflow:hidden}
.page-1{left:0}.page-2{left:402px}.page-3{left:804px}
.abs{position:absolute}
.photo{position:absolute}
.photo-caption{position:absolute;font-size:6px;font-weight:700;color:var(--navy);background:rgba(255,255,255,.75);padding:2px 4px;line-height:1.25}
.photo-caption span{display:block;font-weight:400;font-size:5.5px}
.photo-caption.light{color:var(--white);background:none}
.sand{background:linear-gradient(160deg,var(--sky-a) 0%,var(--sky-b) 45%,var(--sand-a) 70%,var(--sand-b) 100%)}
.stone{background:linear-gradient(180deg,var(--sky-a) 0%,var(--stone-a) 35%,var(--stone-b) 100%)}
.museum{background:linear-gradient(180deg,#c9b394 0%,#8f7356 60%,#5e4a37 100%)}
.campus{background:linear-gradient(180deg,#b7cbe0 0%,#d8c8a8 55%,#9a8a6a 100%)}
.band{position:absolute;left:0;width:100%;top:172px;height:6px;background:var(--navy)}
.footer{position:absolute;left:0;bottom:0;width:100%;height:9px;background:var(--navy);color:var(--white);font-size:4.8px;line-height:9px;padding-left:6px}
.day{position:absolute;background:linear-gradient(180deg,var(--panel-a),var(--panel-b));padding:5px 6px;font-size:4.6px;line-height:1.36;color:var(--ink)}
.day h3{font-size:6.4px;color:var(--blue);margin-bottom:3px;font-weight:700}
.day h4{font-size:4.9px;font-weight:700;margin-top:2px;color:var(--ink)}
.day p{margin-bottom:2px}
.day .overnight{font-weight:700;margin-top:2px}
.day.plain{background:var(--white)}
/* page 1 */
.hero{left:0;top:0;width:396px;height:232px}
.hero-caption{position:absolute;left:8px;top:6px;color:var(--white);font-size:6.5px;font-weight:700;line-height:1.3}
.hero-caption span{font-weight:400;display:block;font-size:5.5px}
.top-sights{position:absolute;left:280px;top:0;width:116px;height:232px;background:rgba(27,55,102,.92);padding:14px 7px 0}
.top-sights h2{font-size:7.8px;font-style:italic;color:var(--white);font-weight:700;margin-bottom:8px;line-height:1.2}
.sight{display:flex;align-items:center;gap:6px;margin-bottom:9px}
.sight .thumb{width:34px;height:27px;flex:none}
.sight span{font-size:5.6px;color:var(--white);font-weight:700}
.title{left:10px;top:240px;font-size:22px;font-weight:700;font-style:italic;color:var(--blue);line-height:1.2}
.subtitle{left:10px;top:271px;font-size:5.6px;color:var(--muted)}
.subtitle b{color:var(--ink)}
.brand{left:318px;top:256px;display:flex;align-items:center;gap:4px}
.brand i{display:block;width:8px;height:8px;background:var(--blue)}
.brand span{font-size:5.4px;font-weight:700;color:var(--blue);line-height:1.1;width:48px}
.focus{left:10px;top:285px;font-size:5.4px;line-height:1.6;color:var(--ink)}
.included{left:10px;top:342px;width:130px}
.included h2{font-size:6.8px;font-weight:700;color:var(--ink);margin-bottom:6px}
.inc{display:flex;align-items:center;gap:8px;height:19px;font-size:5px;color:var(--muted)}
.inc svg{width:10px;height:10px;flex:none;fill:var(--muted)}
.itinerary{left:147px;top:326px;width:241px;height:146px;background:var(--box);border:1px solid #c9ccd2;padding:6px 8px;display:grid;grid-template-columns:1fr 1fr;column-gap:10px;font-size:5.2px;line-height:1.38;color:var(--muted)}
.itinerary b{color:var(--ink);display:block;font-size:5.5px}
.itinerary .entry{margin-bottom:5px}
</style>
</head>
<body>

<section class="page page-1">
  <div class="photo hero sand" role="img" aria-label="Photograph of the Great Pyramid and the Sphinx in the desert at Giza"></div>
  <div class="hero-caption">Pyramid and Sphinx<span>Cairo, Egypt</span></div>
  <aside class="top-sights">
    <h2>Top things to see on tour:</h2>
    <div class="sight"><div class="thumb museum" role="img" aria-label="Cairo Museum statues"></div><span>Cairo Museum</span></div>
    <div class="sight"><div class="thumb stone" role="img" aria-label="Philae Temple"></div><span>Philae Temple</span></div>
    <div class="sight"><div class="thumb stone" role="img" aria-label="Edfu Temple"></div><span>Edfu Temple</span></div>
    <div class="sight"><div class="thumb sand" role="img" aria-label="Valley of the Kings"></div><span>Valley of the Kings</span></div>
    <div class="sight"><div class="thumb stone" role="img" aria-label="Hatshepsut Temple"></div><span>Hatshepsut Temple</span></div>
  </aside>

  <h1 class="abs title">Cairo &amp; Lucor</h1>
  <div class="abs subtitle"><b>8 days</b> | Egypt</div>
  <div class="abs brand"><i></i><span>Open Skies Field Learning</span></div>
  <div class="abs focus">
    <div><b>Main focus subject:</b> History and Anthropology</div>
    <div><b>Related subjects:</b> Geography, Development Studies, Agriculture, Environmental Management</div>
    <div><b>Environmental focus:</b> Impact of climate change on the Nile river basin</div>
  </div>

  <div class="abs included">
    <h2>What's included in price:</h2>
    <div class="inc"><svg viewBox="0 0 10 10"><path d="M5 0.5l1 3.5 4 1.5v1l-4-0.8-0.6 2.3 1.3 1v0.8L5 9.3 3.3 9.8V9l1.3-1-0.6-2.3-4 .8v-1l4-1.5z"/></svg>Air Ticket</div>
    <div class="inc"><svg viewBox="0 0 10 10"><circle cx="5" cy="2" r="1.8"/><path d="M2 10V6a3 3 0 0 1 6 0v4z"/></svg>Full time Tour Director</div>
    <div class="inc"><svg viewBox="0 0 10 10"><rect x="0.5" y="3" width="1.2" height="6"/><rect x="0.5" y="6" width="9" height="1.5"/><rect x="4" y="4" width="5.5" height="2"/><rect x="8.3" y="7" width="1.2" height="2"/></svg>All accommodation</div>
    <div class="inc"><svg viewBox="0 0 10 10"><rect x="2" y="0.5" width="1" height="9"/><rect x="1" y="0.5" width="0.6" height="3"/><rect x="3.4" y="0.5" width="0.6" height="3"/><path d="M6.5 0.5c1.5 0 2 2 2 3.5H7.4v5.5H6.5z"/></svg>Meals</div>
    <div class="inc"><svg viewBox="0 0 10 10"><circle cx="3" cy="2.5" r="1.5"/><circle cx="7" cy="2.5" r="1.5"/><path d="M0.5 9V6.5a2.5 2.5 0 0 1 5 0V9zM4.5 9V6.5a2.5 2.5 0 0 1 5 0V9z"/></svg>Tours led by local expert tour guides</div>
    <div class="inc"><svg viewBox="0 0 10 10"><path d="M0.5 2.5h9v1.6a1 1 0 0 0 0 1.8v1.6h-9V5.9a1 1 0 0 0 0-1.8z"/></svg>Entrance fees to attractions</div>
  </div>

  <div class="abs itinerary">
    <div>
      <div class="entry"><b>Day 1: Arrival at Cairo</b>– Cairo city tour<br>– Pyramid and Sphinx</div>
      <div class="entry"><b>Day 2: Cairo Museum &amp; Khan El Khalili Bazaar</b>– Cairo to Aswan by flight or train</div>
      <div class="entry"><b>Day 3: Embark on Nile Cruise</b>– Visit high dam<br>– Visit unfinished obelisk<br>– Visit Philae Temple</div>
      <div class="entry"><b>Day 4: Nile Cruise</b>– Visit Temple of Kom Ombo<br>– Visit Edfu Temple</div>
    </div>
    <div>
      <div class="entry"><b>Day 5: Nile Cruise</b>– Visit Temple of Karnak<br>– Visit Temple of Luxor</div>
      <div class="entry"><b>Day 6: Disembark from Nile Cruise</b>– Visit Luxor<br>– Colossi of Memnon<br>– Visit Valley of the Kings<br>– Visit Hatshepsut Temple</div>
      <div class="entry"><b>Day 7: Luxor</b>– Visit Colossi of Memnon<br>– Visit Valley of the Kings<br>– Visit Hatshepsut Temple<br>– Luxor to Cairo by train</div>
      <div class="entry"><b>Day 8: Depart for home</b></div>
    </div>
  </div>
  <div class="footer">Email: hello@openskiesfield.example &nbsp;|&nbsp; +971 4 555 0142</div>
</section>

<section class="page page-2">
  <div class="day" style="left:0;top:0;width:192px;height:172px">
    <h3>Day 1 – Arrival at Cairo (L/D)</h3>
    <p><b>Ahlan! Welcome to historical EGYPT!</b></p>
    <p>Upon arrival at Cairo airport, you will be met and assisted through passport control.</p>
    <p>You will then travel to Giza to see the famous Sphinx and visit the Great Pyramids. Giza is the location of the Pyramid of Khufu, also known as the "Great Pyramid" and the "Pyramid of Cheops"; the somewhat smaller Pyramid of Khafre (or Kephren); and the relatively modest-sized Pyramid of Menkaure (or Mykerinus), along with a number of smaller satellite edifices known as "Queens' pyramids". The Great Pyramid was the centrepiece of an elaborate complex, which included several small pyramids, five boat pits, a mortuary temple, a causeway, a valley temple, and many flat-roofed tombs for officials and some members of the royal family. After this, you continue on to Sakkara with lunch at a restaurant en route.</p>
    <p>After lunch, visit the Step Pyramid of Zoser, the oldest pyramid in Egypt. Built by the great architect Imhotep, the Step Pyramid shows the evolution from mastaba type tombs to the pyramid form. Nearby are tombs of kings and nobles dating from the earliest dynasties of the Old Kingdom period. From here you go to the ancient capital of Memphis to see the Alabaster Sphinx and the colossal statue of Ramesses II.</p>
    <p class="overnight">Overnight in Cairo.</p>
  </div>
  <div class="day" style="left:196px;top:0;width:200px;height:58px">
    <h3>Day 2 – Cairo Museum &amp; Bazaar (B/D)</h3>
    <p>After breakfast, you will take a tour to the world famous Egyptian Museum with its 100,000 objects covering 4,000 years of ancient Egyptian civilization, including the treasures of Tutankhamun. You will then immerse into the old souq of Khan El Khalili bazaar.</p>
    <p>In the evening, have a sumptuous dinner before transfer to railway station for departure to Aswan on first class sleeper train.</p>
  </div>
  <div class="photo museum" style="left:196px;top:58px;width:200px;height:114px" role="img" aria-label="Photograph of seated pharaoh statues inside the Cairo Museum"></div>
  <div class="photo-caption" style="left:202px;top:150px">Cairo Museum<span>Cairo, Egypt</span></div>

  <div class="band"></div>

  <div class="photo stone" style="left:0;top:178px;width:144px;height:132px" role="img" aria-label="Photograph of the columns and pylon of Philae Temple"></div>
  <div class="photo-caption" style="left:6px;top:184px">Philae Temple<span>Aswan, Egypt</span></div>
  <div class="day" style="left:144px;top:178px;width:252px;height:132px">
    <h3>Day 3 – Aswan – Nile Cruise (B/L/D)</h3>
    <p>Upon arrival in Aswan, you will be transferred to the Nile Cruise terminal. Embark on your cruise, where you will be welcomed and briefed about your journey on the cruise. Sit back and relax for your tour of Aswan.</p>
    <h4>High dam</h4>
    <p>The high dam is the largest rock-filled dam in the world and one of the most important engineering feats of the 20th century, an artificial lake, Nasser, with a surface of 4,000 sq km behind the dam.</p>
    <h4>Unfinished obelisk</h4>
    <p>The unfinished obelisk is the largest known ancient obelisk, located in the northern region of the stone quarries of ancient Egypt in Aswan. It is unknown which pharaoh created this structure. It is nearly one third larger than any other ancient Egyptian obelisk. If finished it would have measured around 42 m and weighed nearly 1,200 tons.</p>
    <h4>Philae Temple</h4>
    <p>Philae Temple was dismantled and reassembled on Agilika Island about 550 meters from its original home on Philae Island. It is dedicated to the goddess Isis, in a beautiful setting which has been landscaped to match its original site. Its various shrines and sanctuaries include the Vestibule of Nectanebo I, which is used as the entrance to the island.</p>
    <p class="overnight">Overnight on Cruise.</p>
  </div>

  <div class="day" style="left:0;top:310px;width:172px;height:169px">
    <h3>Day 4 – Nile Cruise (B/L/D)</h3>
    <p><b>Breakfast on board.</b></p>
    <p>You will sail towards Luxor via Kom Ombo, Edfu and Esna.</p>
    <h4>Temple of Kom Ombo</h4>
    <p>This is an unusual double temple built during the Ptolemaic dynasty in the Egyptian town of Kom Ombo. Some additions to it were later made during the Roman period. The building is unique because its 'double' design meant that there were courts, halls, sanctuaries and rooms duplicated for two sets of gods. The southern half of the temple was dedicated to the crocodile god Sobek, god of fertility and creator of the world, with Hathor and Khonsu. Meanwhile, the northern part of the temple was dedicated to the falcon god Haroeris, also known as Horus the Elder.</p>
    <h4>Edfu Temple</h4>
    <p>Two splendid granite statues of Horus, who was generally represented as a man with a falcon's head, mark the entrance of this temple which was constructed during the Ptolemaic period from 237 BC. Follow its 10 columns with palm leaves, flowers and well preserved wall paintings as witnesses of the great wealth of the older days. After that, you will return to the Cruise and continue your journey to Luxor.</p>
    <p class="overnight">Overnight on Cruise.</p>
  </div>
  <div class="photo stone" style="left:172px;top:310px;width:224px;height:169px" role="img" aria-label="Photograph of the great pylon gateway of Edfu Temple"></div>
  <div class="photo-caption" style="left:336px;top:452px">Edfu Temple<span>Edfu, Egypt</span></div>
  <div class="footer">Email: hello@openskiesfield.example &nbsp;|&nbsp; +971 4 555 0142</div>
</section>

<section class="page page-3">
  <div class="day" style="left:0;top:0;width:158px;height:172px">
    <h3>Day 5 – Nile Cruise – Luxor (B/L/D)</h3>
    <p><b>Today, you will be cruising into Luxor!</b></p>
    <p>Upon arrival, you will be taken to visit the impressive temples of Karnak and Luxor.</p>
    <h4>Temple of Karnak</h4>
    <p>It is the largest temple in the world. The complex contains a group of temples such as the Great Temple of Amon Ra, the Temple of Khonso, the Ipet Temple, the Temple of Ptah, the Temple of Montho and the Temple of the God Osiris. A 20m high, mud brick enclosure wall surrounds all of these buildings.</p>
    <h4>Temple of Luxor</h4>
    <p>It is close to the Nile and parallel with the riverbank. King Amenhotep III, who reigned 1390-53 BC, built this beautiful temple and dedicated it to Amon Ra, king of the gods, his consort Mut, and their son Khonsu. This temple has been in almost continuous use as a place of worship right up to the present day. It was completed by Tutankhamun and Horemheb, and added to by Ramses II. Towards the rear is a granite shrine dedicated to Alexander the Great.</p>
    <p class="overnight">Overnight on Cruise.</p>
  </div>
  <div class="photo stone" style="left:158px;top:0;width:238px;height:172px" role="img" aria-label="Photograph of the avenue of columns and statues at the Temple of Karnak"></div>
  <div class="photo-caption light" style="left:326px;top:6px">Temple of Karnak<span>Luxor, Egypt</span></div>

  <div class="band"></div>

  <div class="photo sand" style="left:0;top:178px;width:156px;height:132px" role="img" aria-label="Photograph of the desert cliffs and entrance path of the Valley of the Kings"></div>
  <div class="photo-caption" style="left:6px;top:288px">Valley of the Kings<span>Luxor, Egypt</span></div>
  <div class="day" style="left:156px;top:178px;width:240px;height:132px">
    <h3>Day 6 – Luxor – Cairo (B/D)</h3>
    <p>After breakfast, you will disembark from the Nile Cruise and then visit the city of Luxor where you will see:</p>
    <h4>Colossi of Memnon</h4>
    <p>The colossi are two massive stone statues of Pharaoh Amenhotep III. For the past 3,400 years (since 1350 BC), they have stood in the Theban necropolis, across the River Nile from the modern city of Luxor.</p>
    <h4>Valley of the Kings</h4>
    <p>The Valley of the Kings, less often called the Valley of the Gates of the Kings, is a valley in Egypt where, for a period of nearly 500 years from the 16th to 11th century BC, tombs were constructed for the Pharaohs and powerful nobles of the New Kingdom. The valley stands on the West bank of the Nile, opposite Thebes (modern Luxor), within the heart of the Theban Necropolis. The wadi consists of two valleys, East Valley and West Valley.</p>
    <h4>Hatshepsut Temple</h4>
    <p>Hatshepsut, meaning Foremost of Noble Ladies (1508–1458 BC), was the fifth pharaoh of the eighteenth dynasty of Ancient Egypt. She is generally regarded by Egyptologists as one of the most successful pharaohs, reigning longer than any other woman of an indigenous Egyptian dynasty.</p>
    <p>Transfer to Luxor station for sleeper train to Cairo.</p>
  </div>

  <div class="day plain" style="left:0;top:310px;width:184px;height:169px;padding-top:16px">
    <h3>Day 7 – Cairo (B)</h3>
    <p><b>Breakfast on train.</b> Today is your free day to wander around Cairo. You may also choose to visit Alexandria, the beautiful port city at an extra cost of USD100 per person.</p>
    <h3 style="margin-top:14px">Day 8 – Departure (B)</h3>
    <p>After breakfast, free and easy until time to transfer to airport for departure.</p>
  </div>
  <div class="photo campus" style="left:184px;top:310px;width:212px;height:169px" role="img" aria-label="Photograph of the domed main building of Cairo University with its lawns"></div>
  <div class="photo-caption" style="left:334px;top:316px">Cairo University<span>Cairo, Egypt</span></div>
  <div class="footer">Email: hello@openskiesfield.example &nbsp;|&nbsp; +971 4 555 0142</div>
</section>

</body>
</html>
```